Hello my name is Colin, I am Starting a business called Harbor Health and fitness and am in need of a memorable business card.
It is a personal training studio. I have added the logo that i would like to be on the left center om my business card. i would like room left up the top for a heading sentence such as. "Is your body shocking for all the wrong reasons". there must be room left on the right of the logo below the main heading for 3 sub headings.
then under those 3 headings and logo room for another larger heading eg. "give me a call and learn how to eat chocolate, drink bear and have great sex". in what room is left i would like to be used for my contact details, use I'm Colin Fairweather your fitness expert on the left then on the right Phone, Email and website space in at least 12 Point. Very specific i know :) now onto the back, for the back i would like an eye catching graphic and room for one main headline and 3 bullet points centered just write anything i will choose what to put in them when i pick a winner. Thank you very much for sticking through all of that :) i appreciate you taking the time to read it and hopefully undergo designing me a business card.
I can't wait to see the designs!

Target Market(s)

slightly more towards females although it would probably be best if it was targeted towards both sexes

Industry/Entity Type

Training

Requirements
Nice to have
• I would love to see if anyone could come up with a design that would really make my card stand out and be memorable.
Should not have
• tacky fitness photos of abs and muscles etc.

```html
<!DOCTYPE html>
<html lang="en">
<head>
<meta charset="utf-8">
<title>Harbor Health and Fitness – Business Card</title>
<link rel="stylesheet" href="https://fonts.googleapis.com/css2?family=Open+Sans:wght@400;500;600&display=swap">
<style>
  :root {
    --ink-black: #050505;
    --charcoal: #2b2f33;
    --slate: #3d4349;
    --cone-grey: #5c6165;
    --silver: #b9bdbf;
    --spot-white: #eef7f4;
    --band-grey: #a9b0b0;
    --text-dark: #1c1c1c;
    --text-light: #f2f2f2;
    --contact-ice: #d8e8ea;
  }
  html, body {
    margin: 0;
    padding: 0;
    overflow: hidden;
    background: #ffffff;
  }
  .card {
    position: relative;
    width: 1200px;
    height: 720px;
    overflow: hidden;
    font-family: "Open Sans", Arial, sans-serif;
    background: var(--ink-black);
  }
  .card-backdrop {
    position: absolute;
    inset: 0;
  }
  .headline {
    position: absolute;
    left: 155px;
    top: 54px;
    margin: 0;
    font-size: 25px;
    font-weight: 500;
    letter-spacing: 2.4px;
    color: var(--text-dark);
  }
  .brand {
    position: absolute;
    left: 160px;
    top: 100px;
    width: 420px;
    color: var(--text-dark);
    font-weight: 400;
  }
  .brand-name {
    display: block;
    font-size: 112px;
    line-height: 1;
    letter-spacing: -2px;
  }
  .brand-tagline {
    display: block;
    margin: 4px 0 0 96px;
    font-size: 26px;
    letter-spacing: -0.3px;
  }
  .sub-headings {
    position: absolute;
    left: 709px;
    top: 136px;
    margin: 0;
    padding: 0;
    list-style: none;
    color: var(--text-light);
    font-size: 36px;
    line-height: 48px;
    letter-spacing: 4px;
  }
  .introduction {
    position: absolute;
    left: 130px;
    top: 372px;
    width: 420px;
    margin: 0;
    text-align: center;
    color: var(--text-dark);
    font-size: 39px;
    line-height: 56px;
    letter-spacing: -0.8px;
  }
  .introduction .trainer-name {
    display: block;
    font-size: 33px;
    letter-spacing: -1.2px;
  }
  .contact {
    position: absolute;
    left: 606px;
    top: 398px;
    margin: 0;
    font-style: normal;
    color: var(--contact-ice);
    letter-spacing: 3px;
  }
  .contact-line {
    display: block;
  }
  .contact-phone,
  .contact-email {
    font-size: 46px;
    line-height: 62px;
  }
  .contact-web {
    font-size: 37px;
    line-height: 56px;
    letter-spacing: 2.8px;
  }
  .promise {
    position: absolute;
    left: 0;
    top: 628px;
    width: 1200px;
    margin: 0;
    text-align: center;
    font-size: 25px;
    font-weight: 500;
    line-height: 46px;
    letter-spacing: -0.3px;
    color: var(--text-dark);
  }
</style>
</head>
<body>
  <main class="card">
    <svg class="card-backdrop" width="1200" height="720" viewBox="0 0 1200 720" aria-hidden="true">
      <defs>
        <linearGradient id="night-fade" x1="0" y1="0" x2="1" y2="0">
          <stop offset="0" stop-color="#2e3338"/>
          <stop offset="0.55" stop-color="#16181a"/>
          <stop offset="1" stop-color="#020202"/>
        </linearGradient>
        <linearGradient id="silver-sweep" x1="0" y1="0" x2="1" y2="1">
          <stop offset="0" stop-color="#d9dcdd"/>
          <stop offset="1" stop-color="#8d9396"/>
        </linearGradient>
        <linearGradient id="spot-cone" x1="0" y1="0" x2="0" y2="1">
          <stop offset="0" stop-color="#6d7276"/>
          <stop offset="1" stop-color="#4e5357"/>
        </linearGradient>
        <linearGradient id="band-fade" x1="0" y1="0" x2="1" y2="0">
          <stop offset="0" stop-color="#c9cfcf"/>
          <stop offset="1" stop-color="#8e9797"/>
        </linearGradient>
        <radialGradient id="spot-glow" cx="0.5" cy="0.45" r="0.6">
          <stop offset="0" stop-color="#f6fbf9"/>
          <stop offset="1" stop-color="#e6f1ee"/>
        </radialGradient>
      </defs>

      <rect class="night-field" width="1200" height="720" fill="url(#night-fade)"/>

      <path class="silver-sweep" d="M0 0 H120 C60 160 70 380 150 560 C175 620 200 680 215 720 H0 Z" fill="url(#silver-sweep)"/>
      <path class="shadow-sweep" d="M0 360 C40 430 90 560 120 720 H0 Z" fill="var(--slate)"/>

      <path class="spotlight-cone" d="M150 120 C120 260 110 380 170 520 C205 600 225 670 235 720 H480 C490 650 520 560 560 470 C600 380 610 240 605 120 Z" fill="url(#spot-cone)"/>

      <rect class="headline-band" x="140" y="50" width="1060" height="46" fill="url(#band-fade)" opacity="0.95"/>

      <circle class="spotlight" cx="378" cy="110" r="230" fill="url(#spot-glow)"/>

      <g class="dot-rule dot-rule-top" fill="#8a8f92" stroke="#c5c9cb" stroke-width="1">
        <rect x="608" y="359" width="12" height="11"/><rect x="643" y="359" width="12" height="11"/>
        <rect x="678" y="359" width="12" height="11"/><rect x="713" y="359" width="12" height="11"/>
        <rect x="748" y="359" width="12" height="11"/><rect x="783" y="359" width="12" height="11"/>
        <rect x="818" y="359" width="12" height="11"/><rect x="853" y="359" width="12" height="11"/>
        <rect x="888" y="359" width="12" height="11"/><rect x="923" y="359" width="12" height="11"/>
        <rect x="958" y="359" width="12" height="11"/><rect x="993" y="359" width="12" height="11"/>
        <rect x="1028" y="359" width="12" height="11"/><rect x="1063" y="359" width="12" height="11"/>
        <rect x="1098" y="359" width="12" height="11"/>
      </g>
      <g class="dot-rule dot-rule-bottom" fill="#8a8f92" stroke="#c5c9cb" stroke-width="1">
        <rect x="608" y="603" width="12" height="11"/><rect x="643" y="603" width="12" height="11"/>
        <rect x="678" y="603" width="12" height="11"/><rect x="713" y="603" width="12" height="11"/>
        <rect x="748" y="603" width="12" height="11"/><rect x="783" y="603" width="12" height="11"/>
        <rect x="818" y="603" width="12" height="11"/><rect x="853" y="603" width="12" height="11"/>
        <rect x="888" y="603" width="12" height="11"/><rect x="923" y="603" width="12" height="11"/>
        <rect x="958" y="603" width="12" height="11"/><rect x="993" y="603" width="12" height="11"/>
        <rect x="1028" y="603" width="12" height="11"/><rect x="1063" y="603" width="12" height="11"/>
        <rect x="1098" y="603" width="12" height="11"/>
      </g>

      <rect class="promise-band" x="36" y="628" width="1164" height="46" fill="url(#band-fade)" opacity="0.95"/>
    </svg>

    <h1 class="headline">Is your body shocking for all the wrong reasons?</h1>

    <div class="brand">
      <span class="brand-name">Harbor</span>
      <span class="brand-tagline">Health and Fitness</span>
    </div>

    <ol class="sub-headings">
      <li>1 sub heading</li>
      <li>2 sub heading</li>
      <li>3 sub heading</li>
    </ol>

    <p class="introduction">
      I'm
      <span class="trainer-name">COLIN FAIRWEATHER</span>
      your fitness<br>expert
    </p>

    <address class="contact">
      <span class="contact-line contact-phone">944.555.0172</span>
      <span class="contact-line contact-email">Email Address</span>
      <span class="contact-line contact-web">www.yourwebsite.com</span>
    </address>

    <p class="promise">"give me a call and learn how to eat chocolate, drink bear and have great sex"</p>
  </main>
</body>
</html>
```